Redesign Website

I currently have a website www.kelvaromotionrx.com that I would like to have redesigned for esthetics and design limitations with the present platform. I will provide my logo, background logo (attached) , current site, foundation grip PSD.zip (attached) and a questionnaire (attached) from a web design company to provide the input to have an impressive site that pleases the eyes and makes an impact. I would also like the site to be mobile friendly.

IMPORTANT:
- The final PSD must include:
o Homepage Mockup
o Internal Pages Mockup
o Mobile site mockup
o Fonts files used in mockup

Final website will be responsive, using the Foundation Framework. Attached you will find a PSD of the Foundation grid – please use this and include with your final PSD. Here is a link for reference:
http://plimtex.com/article/1053/foundation-s-grid-and-photoshop-what-you-

Target Market(s)

Patients for physical therapy

Industry/Entity Type

It Company

Requirements
Must have
• Pages included in the present site. Photos and design should change.
Nice to have
• Should provide information necessary for patients to schedule an appointment
Should not have
• Should not be difficult to read.

```html
<!DOCTYPE html>
<html lang="en">
<head>
<meta charset="utf-8">
<title>Kelvaro Sports &amp; Orthopedic Physical Therapy</title>
<link rel="stylesheet" href="https://fonts.googleapis.com/css2?family=Open+Sans:wght@300;400;600;700&display=swap">
<style>
:root{
  --maroon:#8a0e0e;
  --maroon-deep:#4a0606;
  --gold:#e9a100;
  --gold-light:#f7c21a;
  --white:#ffffff;
  --text:#666666;
  --heading:#3a3a3a;
  --sky:#8b93d6;
}
*{box-sizing:border-box;margin:0;padding:0}
html,body{width:938px;height:1200px;overflow:hidden}
body{position:relative;background:var(--maroon);font-family:'Open Sans',Arial,sans-serif;color:var(--text)}
.page{position:absolute;left:121px;top:7px;width:693px;height:910px;background:var(--white)}
.brand{position:absolute;left:8px;top:20px;display:flex;align-items:center;gap:6px;font-size:20px;font-weight:600;color:var(--maroon)}
.brand .dot{width:14px;height:14px;border-radius:50%;background:var(--gold)}
.search{position:absolute;left:554px;top:52px;width:129px;height:17px;border:1px solid #cfcfcf;font-size:8px;color:#aaa;padding:3px 5px;display:flex;justify-content:space-between;align-items:center}
.nav{position:absolute;left:7px;top:77px;width:678px;height:44px;background:var(--maroon);display:flex;align-items:center;list-style:none}
.nav li{font-size:9.3px;font-weight:700;color:var(--white);padding:0 4.9px;white-space:nowrap}
.nav li.active{background:linear-gradient(var(--gold-light),var(--gold));height:44px;line-height:44px;width:52px;text-align:center;padding:0;margin-right:5px}
.hero{position:absolute;left:7px;top:125px;width:678px;height:210px;background:linear-gradient(90deg,#6d6e9a 0%,#8e8fb8 35%,#9aa0d8 60%,var(--sky) 100%)}
.hero .title{position:absolute;left:475px;top:80px;font-size:30px;font-weight:300;color:var(--white)}
.hero svg{position:absolute;top:86px}
.welcome{position:absolute;left:0;width:693px;top:351px;text-align:center;font-size:19px;font-weight:400;color:var(--maroon)}
.portrait{position:absolute;left:270px;top:383px;width:156px;height:156px;border-radius:50%;border:4px solid var(--gold);background:radial-gradient(circle at 50% 40%,#e6d6cf,#c9d2e0 70%,#f2f2f2)}
.doctor{position:absolute;left:0;width:693px;top:546px;text-align:center;font-size:17px;font-weight:300;color:var(--gold)}
.bio{position:absolute;left:16px;width:667px;top:585px;text-align:center;font-size:9.8px;line-height:17.4px;font-weight:400;color:var(--text)}
.block-title{position:absolute;top:715px;font-size:13px;font-weight:600;color:var(--heading)}
.appt{position:absolute;left:65px;top:739px;width:271px;height:150px;background:var(--maroon);color:var(--white);text-align:center}
.appt .lead{font-size:9.5px;margin-top:12px}
.appt svg{margin-top:6px}
.appt .btn{display:block;width:204px;height:37px;margin:4px auto 0;background:var(--gold);font-size:12px;font-weight:700;line-height:37px;letter-spacing:.3px}
.appt .note{font-size:7.8px;line-height:13px;margin-top:7px;padding:0 35px}
.news{position:absolute;left:354px;top:739px;width:271px;height:150px;background:linear-gradient(180deg,#8d8e8e,#4b4a48 55%,#272624)}
.news .caption{position:absolute;left:0;bottom:0;width:100%;height:41px;background:rgba(0,0,0,.55);color:var(--white);font-size:9.8px;padding:5px 8px;line-height:17px}
.footer{position:absolute;left:0;top:917px;width:938px;height:283px;background:var(--maroon-deep);color:var(--white)}
.fnav{position:absolute;left:129px;top:20px;list-style:none;font-size:9.2px;font-weight:700;line-height:16.2px}
.contact{position:absolute;left:243px;top:18px;font-size:10px;line-height:17.3px}
.contact strong{font-weight:600}
.fhead{position:absolute;top:20px;font-size:10px;font-weight:600}
.map{position:absolute;left:414px;top:47px;width:217px;height:120px;background:linear-gradient(135deg,#e8e2b4,#f3e36a 50%,#d9d3b8)}
.map-note{position:absolute;left:414px;top:177px;width:220px;font-size:8px;line-height:13px}
.social{position:absolute;left:652px;top:51px;width:153px;list-style:none}
.social li{display:flex;justify-content:space-between;align-items:center;font-size:10px;height:30px}
.social li span.ic{width:16px;height:16px;border-radius:50%;background:var(--white)}
.copy{position:absolute;left:0;width:938px;top:243px;text-align:center;font-size:10px}
</style>
</head>
<body>
<main class="page">
  <div class="brand"><span class="dot"></span>Kelvaro</div>
  <div class="search">Search
    <svg width="8" height="8" viewBox="0 0 8 8"><circle cx="3.2" cy="3.2" r="2.3" fill="none" stroke="#aaa"/><line x1="5" y1="5" x2="7.5" y2="7.5" stroke="#aaa"/></svg>
  </div>
  <ul class="nav">
    <li class="active">Home</li><li>Location</li><li>Hours</li><li>Our Story</li><li>Mission Statement</li><li>Services</li><li>Insurance</li><li>New Patients</li><li>Contact Us</li><li>Testimonials</li><li>Community</li>
  </ul>
  <section class="hero" role="img" aria-label="Snow-capped mountain peak at dusk against a lavender sky">
    <svg style="left:22px" width="26" height="40" viewBox="0 0 26 40"><polyline points="22,3 5,20 22,37" fill="none" stroke="#fff" stroke-width="5"/></svg>
    <div class="title">Kelvaro</div>
    <svg style="left:638px" width="26" height="40" viewBox="0 0 26 40"><polyline points="4,3 21,20 4,37" fill="none" stroke="#fff" stroke-width="5"/></svg>
  </section>
  <h1 class="welcome">Welcome to Kelvaro</h1>
  <div class="portrait" role="img" aria-label="Portrait of the lead physical therapist"></div>
  <h2 class="doctor">Dorian Welk, PT, DPT, MS</h2>
  <p class="bio">Our services are the culmination of 15 years of experience of Dr. Dorian Welk, PT, DPT, MS in the sports and orthopedic physical therapy arena.&nbsp; Dorian directed the rehabilitation services for the largest orthopedic group in Harlow County. He has provided the services for an orthopedic and sports medicine group that had specialists in spine, shoulder, elbow, wrist, hand, hip, knee, ankle and foot surgery and treatment.&nbsp; His expertise is the treatment of any and all sports and orthopedic injuries, whether they are the result of trauma, repetitive movements or postures or the result of a surgical intervention.&nbsp; Dorian Welk, PT, DPT, MS is confident that his extensive knowledge base and manual skills will drive Kelvaro Sports &amp; Orthopedic Physical Therapy to become a keystone in the private practice physical therapy community.</p>
  <h3 class="block-title" style="left:65px">Schedule An Appointment</h3>
  <h3 class="block-title" style="left:354px">News</h3>
  <div class="appt">
    <p class="lead">SELECT YOUR DATE TO GET AN APPOINTMENT</p>
    <svg width="24" height="28" viewBox="0 0 24 28"><rect x="1" y="4" width="22" height="23" fill="#fff"/><rect x="5" y="0" width="3" height="7" fill="#fff"/><rect x="16" y="0" width="3" height="7" fill="#fff"/><g fill="#8a0e0e"><rect x="4" y="11" width="4" height="3"/><rect x="10" y="11" width="4" height="3"/><rect x="16" y="11" width="4" height="3"/><rect x="4" y="16" width="4" height="3"/><rect x="10" y="16" width="4" height="3"/><rect x="16" y="16" width="4" height="3"/><rect x="4" y="21" width="4" height="3"/><rect x="10" y="21" width="4" height="3"/><rect x="16" y="21" width="4" height="3"/></g></svg>
    <span class="btn">SCHEDULE AN APPOINTMENT</span>
    <p class="note">Neque porro quisquam est qui dolorem ipsum quia dolor sit amet, consectetur, adipisci velit..."</p>
  </div>
  <div class="news" role="img" aria-label="Interior of a modern gym with treadmills and exercise equipment">
    <div class="caption"><strong>Opened on</strong><br>September 3, 2013 with state of the art equipment.</div>
  </div>
</main>
<footer class="footer">
  <ul class="fnav">
    <li>Home</li><li>Location</li><li>Hours</li><li>Our Story</li><li>Mission Statement</li><li>Services</li><li>Insurance</li><li>New Patients</li><li>Contact Us</li><li>Testimonials</li><li>Community</li>
  </ul>
  <div class="contact">
    <strong>Kelvaro Sports<br>&amp; Orthopedic Physical Therapy</strong><br>
    218 Brookfield Avenue<br>Suite 4<br>Ashford, Pa 19402<br>DWelk@kelvaromotionrx.com<br>
    <div style="height:5px"></div>
    <strong>Call to discuss your options:</strong><br>
    555.201.4470<br>555.201.4471 (fax)<br>www.kelvaromotionrx.com
  </div>
  <h4 class="fhead" style="left:414px">Get Social With Us</h4>
  <div class="map" role="img" aria-label="Street map showing the clinic location"></div>
  <p class="map-note">Neque porro quisquam est qui dolorem ipsum quia dolor sit amet, consectetur, adipisci velit..."</p>
  <h4 class="fhead" style="left:650px">Get Social With Us</h4>
  <ul class="social">
    <li>Circlehub<span class="ic"></span></li>
    <li>Chirpline<span class="ic"></span></li>
    <li>Workmesh<span class="ic"></span></li>
  </ul>
  <p class="copy">© Company Name ,All Rights Reserved</p>
</footer>
</body>
</html>
```